Geothermal company needs a creative "POW" business card

Manufacturers tend to be boring. We are not! We are a Geothermal Heat Pump company that has over 30 yrs of experience and wants a new look and updated feel. Nothing old (yawn) so get your creative hats on and let's rock!

We want to use the great colors of lime green and navy blue. Our new logo is attached and we're ready to roll. Remember, we're a professional leader in the geothermal industry that needs to make an eye catching and memorable first glance.

```html
<!DOCTYPE html>
<html lang="en">
<head>
<meta charset="utf-8">
<title>Frostline Geo — Business Card</title>
<link rel="stylesheet" href="https://fonts.googleapis.com/css2?family=Roboto+Condensed:wght@400;700&family=Mulish:wght@500;700;800&display=swap">
<style>
  :root {
    --lime: #8dc63f;
    --lime-back: #8cc63f;
    --navy: #1b365d;
    --ink: #2b2b2b;
    --text: #3d3d3d;
    --rule: #d4d4d4;
    --paper: #ffffff;
    --backdrop: #4a4945;
    --mark-deep: #1f4f8c;
    --mark-light: #5aa8dc;
  }
  * { box-sizing: border-box; margin: 0; padding: 0; }
  html, body { width: 1117px; height: 1200px; overflow: hidden; }
  body { background: var(--backdrop); position: relative; font-family: "Mulish", sans-serif; }

  .card { position: absolute; left: 103px; width: 903px; height: 514px; overflow: hidden; }
  .card--front { top: 60px; background: var(--paper); }
  .card--back { top: 623px; background: var(--lime-back); }

  .brand-dot {
    position: absolute; left: 54px; top: 54px; width: 134px; height: 134px; border-radius: 50%;
    background: radial-gradient(circle at 35% 30%, var(--mark-light), var(--mark-deep));
  }
  .brand-name {
    position: absolute; left: 224px; top: 60px;
    font-family: "Roboto Condensed", sans-serif; font-weight: 700;
    font-size: 72px; line-height: 1; color: var(--lime); letter-spacing: -0.5px;
  }
  .brand-tagline {
    position: absolute; left: 226px; top: 148px;
    font-family: "Roboto Condensed", sans-serif; font-weight: 400;
    font-size: 20px; color: var(--navy);
  }
  .divider {
    position: absolute; left: 0; top: 256px; width: 100%; height: 4px;
    background: linear-gradient(90deg, transparent, var(--rule) 15%, var(--rule) 85%, transparent);
  }

  .person { position: absolute; left: 70px; top: 280px; }
  .person__name { font-weight: 800; font-size: 33px; color: var(--lime); letter-spacing: 0.3px; }
  .person__role { font-weight: 500; font-size: 25px; color: var(--navy); margin-top: 2px; }
  .person__address { font-weight: 500; font-size: 23px; color: var(--text); line-height: 1.42; margin-top: 22px; }

  .contact { position: absolute; right: 48px; top: 278px; list-style: none; text-align: right; }
  .contact li {
    display: flex; justify-content: flex-end; align-items: center; gap: 8px;
    font-weight: 500; font-size: 23px; color: var(--text); height: 43px;
  }
  .contact svg { width: 18px; height: 18px; fill: var(--navy); }
  .contact .accent { color: var(--lime); }

  .edge { position: absolute; left: 0; bottom: 0; width: 100%; height: 44px; }

  .back-dot {
    position: absolute; left: 43px; top: 82px; width: 352px; height: 352px; border-radius: 50%;
    background: radial-gradient(circle at 35% 30%, var(--mark-light), var(--mark-deep));
  }
  .back-url {
    position: absolute; left: 452px; top: 238px;
    font-weight: 800; font-size: 29px; letter-spacing: 2.2px; color: var(--ink);
  }
</style>
</head>
<body>
  <section class="card card--front" aria-label="Business card front">
    <div class="brand-dot"></div>
    <div class="brand-name">Frostline Geo</div>
    <div class="brand-tagline">Manufacturer of Geothermal Heat Pumps for the North</div>
    <div class="divider"></div>

    <div class="person">
      <div class="person__name">Ray Lindqvist</div>
      <div class="person__role">CEO</div>
      <div class="person__address">18 N Birch Ln<br>Lakeview, MN 55010</div>
    </div>

    <ul class="contact">
      <li><svg viewBox="0 0 24 24"><path d="M6.6 10.8a15 15 0 006.6 6.6l2.2-2.2a1 1 0 011-.25 11.4 11.4 0 003.6.57 1 1 0 011 1V20a1 1 0 01-1 1A17 17 0 013 4a1 1 0 011-1h3.5a1 1 0 011 1c0 1.25.2 2.45.57 3.57a1 1 0 01-.25 1z"/></svg>(555) 014-2200</li>
      <li><svg viewBox="0 0 24 24"><path d="M5 11l1.5-4.5A2 2 0 018.4 5h7.2a2 2 0 011.9 1.5L19 11a2 2 0 012 2v5h-2v2h-3v-2H8v2H5v-2H3v-5a2 2 0 012-2zm2.2 0h9.6l-1-3H8.2zM6.5 16a1.5 1.5 0 100-3 1.5 1.5 0 000 3zm11 0a1.5 1.5 0 100-3 1.5 1.5 0 000 3z"/></svg>(555) 014-2201</li>
      <li><svg viewBox="0 0 24 24"><path d="M3 6h18v12H3zm2 2v.4l7 4.6 7-4.6V8l-7 4.5z"/></svg>raylindqvist@frostlinegeo.com</li>
      <li><svg viewBox="0 0 24 24"><path d="M12 2a10 10 0 100 20 10 10 0 000-20zm6.9 9h-3a15 15 0 00-1.3-5.7A8 8 0 0118.9 11zM12 4.1c.9 1.2 1.8 3.5 1.9 6.9h-3.8c.1-3.4 1-5.7 1.9-6.9zM9.4 5.3A15 15 0 008.1 11h-3a8 8 0 014.3-5.7zM5.1 13h3a15 15 0 001.3 5.7A8 8 0 015.1 13zm6.9 6.9c-.9-1.2-1.8-3.5-1.9-6.9h3.8c-.1 3.4-1 5.7-1.9 6.9zm2.6-1.2a15 15 0 001.3-5.7h3a8 8 0 01-4.3 5.7z"/></svg>www.<span class="accent">frostlinegeo</span>.com</li>
    </ul>

    <svg class="edge" viewBox="0 0 903 44" preserveAspectRatio="none" aria-hidden="true">
      <defs>
        <pattern id="teeth" width="22" height="44" patternUnits="userSpaceOnUse">
          <polygon points="0,14 11,0 22,14 22,44 0,44" fill="#1b365d"/>
        </pattern>
      </defs>
      <rect width="903" height="44" fill="url(#teeth)"/>
    </svg>
  </section>

  <section class="card card--back" aria-label="Business card back">
    <div class="back-dot"></div>
    <div class="back-url">www.frostlinegeo.com</div>
  </section>
</body>
</html>
```